Web Design Project: Need three pages designed, all for same site

Hello,

I am creating a new website that needs a clean, professional look. I need three of the pages designed for the site- all three will have the same header and footer, same brand, same top menu. These three pages represent three unique pages and unique functionality that will allow me to map out the website and then come back here and post a job for the rest of the pages.

The three pages are the Home page, the Profile Page, and the Results page.

I want an extremely simple design for these pages- my goal is for these pages to be rendered almost entirely in "code" with absolute minimal graphics- so use square corners instead of rounded ones, and simple graphic design elements that can be encoded are required.

I need a completely uncompressed PSD file of each of these pages. I want a fixed width site, with some sort of background that looks like a slight gradient up to the edge of the site to make a nice impact on the screen- look at www.plorvex.net for an example of what I am talking about. Also- the visible page should be the same width as that site.

Besides the background edge gradient framing the outside of the site, I would prefer if the only graphical elements are the site logo and a couple of small open-source icons for email and expansion with a "plus" symbol. A background image may be alright if the design is really good and the image is small so it can be quickly loaded.

I want very clean design, very simple. I will have these pages converted to HTML by a separate group.

One Bar Ad Placeholder should be located on every page in a common placement at the top- 728 by 90

Links that should be included in the main navigation bar at the top of the pages:

1. Home
2. About Us
3. Attorney Information
4. Medical Providers- Click Here To List Your Office For Free!

The Medical Providers link should be made to stand out- that is the call to action for medical providers to sign up on the site.

Other links that should be accounted for on all pages:

Login button
Username: (input field)
Password: (input field)
Forgot Login Info?
Create Account
Contact Us
Privacy Policy
Facebook Like
Google +
Linked-In logo
Twitter

Requirements for each individual page:

Home Page:

This will be the home page for the site. It will contain all of the links off of it for the main site menu and navigation elements placed here will appear throughout the site. It will also have a login function at the top right and a logo in the top left.

It will have a search function dominating the left side of the home page consisting of two search input areas:

1. An open search field bar with a Sentence "Open Search by Category and city, or Provider Name: (search input field)"

2. A search panel with address, city, state, zip and two categories of drop down search screening.

The right side of the page will have a placeholder for a youtube introduction video and some basic instructions above and below it.

Essentially, the home page is an introduction to the site and an immediate call to action to use the site for what it is intended to be used for- searching for doctors.

Profile Page:

This will be a page that is used to show the profile of the provider that has been selected. This page must be a format that can be used with all providers listed, no matter how much information each chooses to list. I want a clean appearance and placeholder text will be used to show the placement of various elements on the page. This page will be automatically generated by each provider's information with the same layout for all providers. The information included in the design should be:

Logo
Office name and specialty
Location addresses
Billing Address
Photographs of doctors with their name and specialty
Review average with number of reviews, date of oldest review, and average rating.
Individual Reviews with star rating and synopsis

Results Page:

This is a grid to display four account types as they will be listed- simple page-wide results bars displaying listings, like any search-results driven site. Each result will be clickable to expand it and show more information, so each entry on the page will need to be designed both as closed and the open panel position showing more information. Each result will build on the lesser one before it. This design will be converted to a grid that will be rendered in code, so they should be fairly simple.

That's it.

I am not looking for some complex design, or some loud website layout. I want a simple, functional, clean and professional website for my company. I will want this design to be converted to HTML code, so remember- use fonts that are common to the web. Professional, clean layout is the key here.

I will attach a logo file that you can download in AI 4 format. I do not want it altered.

I will also attach a list of menu items for the menu bar and links that will need to be on every page. For now, simply use placeholder words for them.
Updates

I added the links and menu items I need on all pages to make the top navigation and bottom footer.  

Target Market(s)

Attorneys and their clients

Industry/Entity Type

Graphic Design

Requirements
Must have
• Clear usability

```html
<!DOCTYPE html>
<html lang="en">
<head>
<meta charset="utf-8">
<title>CareAhead – Home</title>
<link rel="stylesheet" href="https://fonts.googleapis.com/css2?family=Roboto:ital,wght@0,300;0,400;0,500;0,700;1,400&display=swap">
<style>
:root{
  --page-bg:#e8e8e8;
  --sheet:#ffffff;
  --brand:#1c63ad;
  --brand-dark:#17558f;
  --ink:#222222;
  --muted:#8a8a8a;
  --field-border:#d9d9d9;
  --panel:#ededed;
  --band:#e0e0e0;
  --banner:#bdbdbd;
  --banner-text:#d9d9d9;
  --rule:#d0d0d0;
}
*{box-sizing:border-box;margin:0;padding:0}
html,body{width:1200px;height:800px;overflow:hidden}
body{background:var(--page-bg);font-family:"Roboto",Arial,sans-serif;color:var(--ink);position:relative}
.sheet{position:absolute;left:193px;top:0;width:815px;height:800px;background:var(--sheet);border-left:1px solid #d6d6d6;border-right:1px solid #d6d6d6}
.abs{position:absolute}
a{color:inherit;text-decoration:none}

/* login */
.login-field{position:absolute;top:6px;height:24px;width:104px;border:1px solid var(--field-border);border-radius:2px;font-size:10px;color:var(--muted);padding:6px 14px;background:#fff}
.login-button{position:absolute;left:792px;top:6px;width:32px;height:24px;background:var(--brand);border-radius:2px}
.login-link{position:absolute;top:12px;font-size:10px;color:#333}

/* brand */
.brand{position:absolute;left:224px;top:46px;display:flex;align-items:center;gap:8px;color:var(--brand-dark);font-size:30px;font-weight:400;letter-spacing:-0.5px}
.brand-mark{width:16px;height:16px;background:var(--brand-dark)}

/* nav */
.main-nav{position:absolute;top:60px;font-size:13px;color:var(--ink)}
.nav-current{position:absolute;left:456px;top:46px;width:35px;height:2px;background:var(--brand)}
.cta{color:var(--brand)}
.cta-star{color:var(--brand);font-size:14px;position:relative;top:-6px;margin-right:2px}

/* banner */
.banner-band{position:absolute;left:194px;top:104px;width:813px;height:88px;background:var(--band)}
.banner{position:absolute;left:308px;top:112px;width:582px;height:72px;background:var(--banner);color:var(--banner-text);font-size:22px;font-weight:300;display:flex;align-items:center;justify-content:center}

/* social */
.social{position:absolute;top:201px;display:flex;gap:4px;align-items:center;font-size:9px}
.social-btn{height:16px;border:1px solid #c9c9c9;border-radius:2px;background:#f3f3f3;padding:0 5px;display:flex;align-items:center;gap:4px;font-weight:700;color:#333}
.social-dot{width:9px;height:9px;background:#8b9bb4}
.social-count{height:16px;border:1px solid #c9c9c9;border-radius:2px;background:#fff;padding:0 4px;display:flex;align-items:center;color:#333}

/* headline */
.headline{position:absolute;left:194px;top:242px;width:813px;text-align:center;color:var(--brand);font-size:19px;font-weight:300;line-height:23px}

/* search */
.search-panel{position:absolute;left:224px;top:311px;width:496px;height:332px;background:var(--panel);border-radius:6px}
.panel-title{position:absolute;font-size:14.5px;font-weight:500;color:var(--brand)}
.divider{position:absolute;left:224px;top:404px;width:496px;height:3px;background:#fff}
.field{position:absolute;height:31px;background:#fff;border:1px solid var(--field-border);border-radius:2px;font-size:11.5px;color:#777;padding:0 15px;display:flex;align-items:center}
.field.big{height:48px;font-size:12.5px;color:#666}
.select-arrow{position:absolute;right:0;top:5px;bottom:5px;width:30px;border-left:1px solid #e3e3e3;display:flex;align-items:center;justify-content:center;color:#bbb;font-size:9px}
.search-button{position:absolute;width:40px;height:32px;background:var(--brand);border-radius:2px;display:flex;align-items:center;justify-content:center}

/* about card */
.about-card{position:absolute;left:736px;top:311px;width:240px;height:260px;background:#fff;border:1px solid #dcdcdc;border-radius:6px}
.read-more{position:absolute;left:904px;top:330px;font-size:10px;font-style:italic;color:var(--muted)}
.video{position:absolute;left:754px;top:354px;width:205px;height:136px;background:#000}
.video-bar{position:absolute;left:754px;top:481px;width:205px;height:9px;background:#d8d8d8}
.about-text{position:absolute;left:753px;top:503px;width:205px;font-size:9px;line-height:11.5px;color:#222}

/* footer */
.footer-link{position:absolute;top:703px;font-size:10px;color:var(--muted)}
.footer-rule{position:absolute;left:208px;top:722px;width:784px;height:1px;background:var(--rule)}
.footer-active{position:absolute;left:846px;top:721px;width:61px;height:2px;background:var(--brand)}
</style>
</head>
<body>
<div class="sheet"></div>

<header>
  <div class="login-field" style="left:568px">Name</div>
  <div class="login-field" style="left:680px">Password</div>
  <div class="login-button">
    <svg width="32" height="24" viewBox="0 0 32 24" aria-hidden="true">
      <rect x="11" y="11" width="10" height="8" fill="#fff"/>
      <path d="M13 11 V8 a3 3 0 0 1 6 0" fill="none" stroke="#fff" stroke-width="1.8"/>
      <rect x="15.3" y="13.5" width="1.4" height="3" fill="#1c63ad"/>
    </svg>
  </div>
  <a class="login-link" style="left:838px" href="#">Forgot Login info?</a>
  <a class="login-link" style="left:921px" href="#">Create account</a>

  <div class="brand"><span class="brand-mark"></span>CareAhead</div>

  <nav>
    <div class="nav-current"></div>
    <a class="main-nav" style="left:456px" href="#">Home</a>
    <a class="main-nav" style="left:516px" href="#">About Us</a>
    <a class="main-nav" style="left:595px" href="#">Attorney Information</a>
    <a class="main-nav" style="left:730px;top:54px" href="#"><span class="cta-star">*</span><span class="cta">Medical Providers - List Your Office</span> for Free!</a>
  </nav>
</header>

<div class="banner-band"></div>
<div class="banner">Banner 728x90px</div>

<div class="social" style="left:570px"><span class="social-btn"><span class="social-dot"></span>Like</span><span class="social-count">15k</span></div>
<div class="social" style="left:650px"><span class="social-btn"><span class="social-dot"></span>Follow @plorvex</span><span class="social-count">28K followers</span></div>
<div class="social" style="left:808px"><span class="social-btn"><span class="social-dot"></span>+1</span><span class="social-count">203</span></div>
<div class="social" style="left:883px"><span class="social-btn"><span class="social-dot"></span>Follow</span><span class="social-count">3,102</span></div>

<h1 class="headline">CareAhead is the Nationwide Online Directory Of Doctors and<br>Medical Providers that Provide Services on a Lien or Letter of Protection.</h1>

<section class="search-panel"></section>
<h2 class="panel-title" style="left:248px;top:325px">Quick Search in a City or Zip Code</h2>
<div class="field big" style="left:232px;top:351px;width:480px">Input Medical Provider Category or Name and City, State or Zip Code</div>
<div class="search-button" style="left:664px;top:359px">
  <svg width="18" height="18" viewBox="0 0 18 18" aria-hidden="true"><circle cx="7.5" cy="7.5" r="5.5" fill="none" stroke="#fff" stroke-width="2.2"/><line x1="11.5" y1="11.5" x2="16" y2="16" stroke="#fff" stroke-width="2.6" stroke-linecap="round"/></svg>
</div>
<div class="divider"></div>
<h2 class="panel-title" style="left:248px;top:428px">Advanced Search</h2>
<div class="field" style="left:232px;top:456px;width:480px">Category<span class="select-arrow">▼</span></div>
<div class="field" style="left:232px;top:504px;width:232px">Address</div>
<div class="field" style="left:480px;top:504px;width:232px">City</div>
<div class="field" style="left:232px;top:552px;width:480px">Screen by Medical Provider Network<span class="select-arrow">▼</span></div>
<div class="field" style="left:232px;top:600px;width:232px">State</div>
<div class="field" style="left:480px;top:600px;width:168px">Zip</div>
<div class="search-button" style="left:664px;top:599px">
  <svg width="18" height="18" viewBox="0 0 18 18" aria-hidden="true"><circle cx="7.5" cy="7.5" r="5.5" fill="none" stroke="#fff" stroke-width="2.2"/><line x1="11.5" y1="11.5" x2="16" y2="16" stroke="#fff" stroke-width="2.6" stroke-linecap="round"/></svg>
</div>

<aside class="about-card"></aside>
<h2 class="panel-title" style="left:753px;top:325px">What we do?</h2>
<a class="read-more" href="#">Read more &gt;</a>
<div class="video" role="img" aria-label="Introduction video player"></div>
<div class="video-bar"></div>
<p class="about-text">Lorem ipsum dolor sit amet, consectetur adipiscing elit. Etiam sagittis tempor massa in mattis. Fusce scelerisque sapien nec quam faucibus pulvinar et sit amet nisi.</p>

<footer>
  <a class="footer-link" style="left:223px" href="#">Home</a>
  <a class="footer-link" style="left:278px" href="#">About Us</a>
  <a class="footer-link" style="left:348px" href="#">Attorney Information</a>
  <a class="footer-link" style="left:468px;top:697px;color:#222" href="#"><span class="cta-star" style="font-size:12px;top:-3px">*</span><span class="cta">Medical Providers - List Your Office</span> for Free!</a>
  <a class="footer-link" style="left:847px;top:705px;color:#333" href="#">Privacy Policy</a>
  <a class="footer-link" style="left:929px;top:705px" href="#">Contact Us</a>
  <div class="footer-rule"></div>
  <div class="footer-active"></div>
</footer>
</body>
</html>
```